Brisa Deck (brisadeckglidepanels.com)

We are looking for a redesign of the entire site. We'd like to first drill down a home page design and make sure the aesthetic fits the brand, then we want to scale out the rest of the pages. The site is a basic lead generation site that focuses on selling Synthetic Ice rinks. There are two components, residential rinks, and commercial rinks. We want the primary focus to be on selling commercial rinks and the secondary to be on residential rinks.

```html
<!DOCTYPE html>
<html lang="en">
<head>
<meta charset="utf-8">
<title>Brisa Deck – Synthetic Ice Rinks</title>
<link href="https://fonts.googleapis.com/css2?family=Outfit:wght@500;600;700&family=Montserrat:wght@400;500;600;700&display=swap" rel="stylesheet">
<style>
:root{
  --red:#c8202f;
  --navy:#1d3a6b;
  --ink:#111418;
  --body:#3b3f46;
  --muted:#7b8088;
  --ice-bg:#eef5fc;
  --rose-bg:#fdf1f3;
  --footer:#1e1f22;
  --white:#ffffff;
  --line:#e3e6ea;
}
*{box-sizing:border-box;margin:0;padding:0}
html,body{width:1200px;height:4644px;overflow:hidden}
body{position:relative;background:var(--white);font-family:"Montserrat",sans-serif;color:var(--body)}
h1,h2,h3{font-family:"Outfit",sans-serif;color:var(--ink)}
.abs{position:absolute}

/* header */
.site-header{position:absolute;left:0;top:0;width:1200px;height:88px;background:var(--white);z-index:2}
.follow{left:128px;top:12px;font-size:11px;color:var(--body);display:flex;align-items:center;gap:10px}
.follow svg{width:16px;height:16px}
.nav-left,.nav-right{top:56px;display:flex;gap:42px;font-size:14px;font-weight:500;color:var(--ink)}
.nav-left{left:128px}
.nav-right{left:820px;gap:96px}
.nav-left .active{border-bottom:2px solid var(--red);padding-bottom:6px}
.brand{left:448px;top:14px;width:320px;height:50px;display:flex;align-items:center;justify-content:center;gap:12px}
.brand-mark{width:20px;height:20px;background:var(--red)}
.brand-name{font-family:"Outfit",sans-serif;font-weight:700;font-size:34px;color:var(--navy);letter-spacing:1px}
.search{left:820px;top:10px;width:172px;height:26px;border:1px solid var(--line);border-radius:13px}
.search svg{position:absolute;right:9px;top:6px;width:13px;height:13px}
.utility{left:1020px;top:10px;display:flex;gap:16px}
.utility svg{width:20px;height:20px}

/* hero */
.hero{position:absolute;left:0;top:88px;width:1200px;height:660px}
.hero-photo{position:absolute;inset:0;background:linear-gradient(100deg,#f2f6fa 0%,#e4ecf3 45%,#c9d6e2 70%,#8d9bab 100%)}
.hero h1{position:absolute;left:128px;top:96px;width:600px;font-size:46px;line-height:1.08;font-weight:700;white-space:nowrap}
.hero p{position:absolute;left:128px;top:232px;width:400px;font-size:13px;line-height:1.6;color:var(--body)}
.btn{display:inline-flex;align-items:center;justify-content:center;font-size:12px;font-weight:700;letter-spacing:.6px;text-transform:uppercase;height:42px;padding:0 26px}
.btn-red{background:var(--red);color:var(--white)}
.btn-outline{border:2px solid var(--navy);color:var(--navy);background:transparent}
.hero .actions{position:absolute;left:128px;top:396px;display:flex;gap:48px}
.hero .actions .btn{width:168px}
.arrows{display:flex;gap:14px}
.round{width:40px;height:40px;border-radius:50%;display:flex;align-items:center;justify-content:center}
.round svg{width:14px;height:14px}
.round-outline{border:2px solid var(--navy);color:var(--navy)}
.round-red{background:var(--red);color:var(--white)}
.hero .arrows{position:absolute;left:128px;top:536px}

/* about */
.about-photo{left:128px;top:848px;width:544px;height:416px;background:linear-gradient(90deg,#3a3330 0%,#5b5049 48%,#2b3c5a 52%,#6e86a5 100%)}
.section-title{font-size:52px;font-weight:600}
.about h2{position:absolute;left:840px;top:900px}
.about p{position:absolute;left:728px;top:980px;width:352px;font-size:14px;line-height:1.7;text-align:right}
.about .btn{position:absolute;left:904px;top:1170px;width:176px}

/* rinks */
.rinks-res{position:absolute;left:0;top:1368px;width:1200px;height:752px;background:var(--ice-bg)}
.center-title{position:absolute;left:0;width:1200px;text-align:center}
.center-copy{position:absolute;left:300px;width:600px;text-align:center;font-size:14px;line-height:1.7}
.rink-photo{position:absolute;left:208px;width:784px;height:308px}
.res-photo{top:272px;background:linear-gradient(180deg,#d9dcdf 0%,#eef0f2 35%,#c9cfd6 48%,#f3e9d9 62%,#f6f4f1 100%)}
.com-photo{top:2400px;background:linear-gradient(180deg,#0e1a25 0%,#1f3a46 40%,#3b5a66 55%,#d7e1e8 70%,#eef2f5 100%)}
.side-arrow{position:absolute;width:40px;height:40px;border-radius:50%;border:2px solid var(--navy);color:var(--navy);display:flex;align-items:center;justify-content:center;background:var(--white)}
.side-arrow.red{border-color:var(--red);color:var(--red)}
.side-arrow svg{width:14px;height:14px}

/* why */
.why{position:absolute;left:0;top:2888px;width:1200px;height:632px;background:var(--rose-bg)}
.why h2{position:absolute;left:128px;top:184px}
.why p{position:absolute;left:128px;top:264px;width:420px;font-size:14px;line-height:1.7}
.feature{position:absolute;width:208px;height:208px;background:var(--white);box-shadow:0 6px 20px rgba(0,0,0,.12);padding:28px 20px 0;text-align:center}
.feature svg{width:40px;height:40px;margin:0 auto;display:block}
.feature h3{font-family:"Montserrat",sans-serif;font-size:15px;font-weight:700;margin:12px 0 10px;color:var(--navy)}
.feature span{font-size:12px;line-height:1.6;display:block;color:var(--body)}

/* testimonials */
.testimonials h2{position:absolute;left:0;top:3616px;width:1200px;text-align:center}
.review{position:absolute;top:3752px;width:440px;height:290px;background:var(--white);box-shadow:0 6px 22px rgba(0,0,0,.1);padding:36px 40px}
.review .who{display:flex;align-items:center;gap:14px}
.avatar{width:62px;height:62px;border-radius:50%;background:linear-gradient(135deg,#c9ced4,#8e96a0)}
.who b{display:block;font-size:12px;color:var(--ink);margin-bottom:4px}
.stars{color:#f2b21b;font-size:14px;letter-spacing:1px}
.quote{position:absolute;right:40px;top:24px;font-family:"Outfit",sans-serif;font-size:110px;line-height:1;color:transparent;-webkit-text-stroke:2px var(--red)}
.review p{margin-top:28px;font-size:14px;line-height:1.7}
.t-arrow{position:absolute;width:26px;height:26px;border-radius:50%;background:var(--white);box-shadow:0 2px 8px rgba(0,0,0,.15);display:flex;align-items:center;justify-content:center;color:var(--red)}
.t-arrow svg{width:10px;height:10px}

/* footer */
.site-footer{position:absolute;left:0;top:4148px;width:1200px;height:496px;background:var(--footer);color:var(--white)}
.site-footer .brand{left:440px;top:124px}
.site-footer .brand-name{color:var(--white)}
.site-footer .brand-mark{background:var(--white)}
.contact{position:absolute;top:240px;display:flex;align-items:center;gap:14px;font-size:12px;letter-spacing:.5px}
.contact .ic{width:40px;height:40px;border-radius:50%;background:var(--navy);display:flex;align-items:center;justify-content:center}
.contact .ic svg{width:18px;height:18px}
.foot-links{position:absolute;top:320px;left:0;width:1200px;font-size:13px}
.foot-links a{position:absolute;color:var(--white);text-decoration:none}
.copyright{position:absolute;left:0;top:460px;width:1200px;text-align:center;font-size:11px;color:#b9bcc1}
</style>
</head>
<body>

<header class="site-header">
  <div class="abs follow">Follow Us On
    <svg viewBox="0 0 16 16"><circle cx="8" cy="8" r="7" fill="none" stroke="#1d3a6b" stroke-width="1.5"/></svg>
    <svg viewBox="0 0 16 16"><rect x="1.5" y="1.5" width="13" height="13" rx="3" fill="none" stroke="#1d3a6b" stroke-width="1.5"/></svg>
  </div>
  <nav class="abs nav-left"><span class="active">Home</span><span>About</span><span>Residential Rinks</span></nav>
  <div class="abs brand"><span class="brand-mark"></span><span class="brand-name">BRISA DECK</span></div>
  <div class="abs search"><svg viewBox="0 0 14 14"><circle cx="6" cy="6" r="4.5" fill="none" stroke="#7b8088" stroke-width="1.5"/><path d="M9.5 9.5L13 13" stroke="#7b8088" stroke-width="1.5"/></svg></div>
  <div class="abs utility">
    <svg viewBox="0 0 20 20"><path d="M10 17S3 12.5 3 7.5A3.5 3.5 0 0 1 10 6a3.5 3.5 0 0 1 7 1.5C17 12.5 10 17 10 17z" fill="none" stroke="#1d3a6b" stroke-width="1.6"/></svg>
    <svg viewBox="0 0 20 20"><path d="M4 7h12l-1 10H5z M7 7V5a3 3 0 0 1 6 0v2" fill="none" stroke="#1d3a6b" stroke-width="1.6"/></svg>
  </div>
  <nav class="abs nav-right"><span>Commercial Rinks</span><span>Contact Us</span></nav>
</header>

<section class="hero">
  <div class="hero-photo" role="img" aria-label="Young hockey player in a red jersey skating on a synthetic ice rink"></div>
  <h1>The Ultimate Synthetic<br>Ice Experience</h1>
  <p>Lorem Ipsum is simply dummy text of the printing and typesetting industry. Lorem Ipsum has been the industry's standard dummy text ever since the 1500s, when an unknown printer took a galley of type and scrambled it to make a type specimen book.</p>
  <div class="actions"><span class="btn btn-red">Contact Us</span><span class="btn btn-outline">Shop Now</span></div>
  <div class="arrows">
    <span class="round round-outline"><svg viewBox="0 0 14 14"><path d="M9 2L4 7l5 5" fill="none" stroke="currentColor" stroke-width="2"/></svg></span>
    <span class="round round-red"><svg viewBox="0 0 14 14"><path d="M5 2l5 5-5 5" fill="none" stroke="currentColor" stroke-width="2"/></svg></span>
  </div>
</section>

<section class="about">
  <div class="abs about-photo" role="img" aria-label="Family watching hockey at home beside players on an indoor rink"></div>
  <h2 class="section-title">About Us</h2>
  <p>Lorem Ipsum is simply dummy text of the printing and typesetting industry. Lorem Ipsum has been the industry's standard dummy text ever since the 1500s, when an unknown printer took a galley of type and scrambled it to make a type specimen book.</p>
  <span class="btn btn-red">Learn More</span>
</section>

<section class="rinks-res">
  <h2 class="section-title center-title" style="top:108px">Residential Rinks</h2>
  <p class="center-copy" style="top:180px">Lorem Ipsum is simply dummy text of the printing and typesetting industry. Lorem Ipsum has been the industry's standard dummy text ever since the 1500s.</p>
  <div class="rink-photo res-photo" role="img" aria-label="Home synthetic ice rink with boards and a hockey goal"></div>
  <span class="side-arrow" style="left:140px;top:406px"><svg viewBox="0 0 14 14"><path d="M9 2L4 7l5 5" fill="none" stroke="currentColor" stroke-width="2"/></svg></span>
  <span class="side-arrow" style="left:1020px;top:406px"><svg viewBox="0 0 14 14"><path d="M5 2l5 5-5 5" fill="none" stroke="currentColor" stroke-width="2"/></svg></span>
  <span class="btn btn-outline abs" style="left:516px;top:614px;width:168px">Learn More</span>
</section>

<section class="rinks-com">
  <h2 class="section-title center-title" style="top:2222px">Commercial Rinks</h2>
  <p class="center-copy" style="top:2292px">Lorem Ipsum is simply dummy text of the printing and typesetting industry. Lorem Ipsum has been the industry's standard dummy text ever since the 1500s.</p>
  <div class="rink-photo com-photo" role="img" aria-label="Commercial synthetic ice arena with stands and a hockey goal"></div>
  <span class="side-arrow red" style="left:140px;top:2534px"><svg viewBox="0 0 14 14"><path d="M9 2L4 7l5 5" fill="none" stroke="currentColor" stroke-width="2"/></svg></span>
  <span class="side-arrow red" style="left:1020px;top:2534px"><svg viewBox="0 0 14 14"><path d="M5 2l5 5-5 5" fill="none" stroke="currentColor" stroke-width="2"/></svg></span>
  <span class="btn btn-red abs" style="left:516px;top:2746px;width:168px">Learn More</span>
</section>

<section class="why">
  <h2 class="section-title">Why Choose Us</h2>
  <p>Lorem Ipsum is simply dummy text of the printing and typesetting industry. Lorem Ipsum has been the industry's standard dummy text ever since the 1500s, when an unknown printer took a galley of type and scrambled it to make a type specimen book. It has survived not only five centuries, but also the leap into electronic typesetting, remaining essentially unchanged.</p>
  <div class="feature" style="left:628px;top:100px">
    <svg viewBox="0 0 40 40" fill="none" stroke="#1d3a6b" stroke-width="2"><circle cx="20" cy="15" r="9"/><path d="M14 23l-3 12 9-4 9 4-3-12"/></svg>
    <h3>Quality</h3><span>Lorem Ipsum is simply dummy text of the printing and typesetting industry.</span>
  </div>
  <div class="feature" style="left:844px;top:100px">
    <svg viewBox="0 0 40 40" fill="none" stroke="#1d3a6b" stroke-width="2"><rect x="6" y="8" width="28" height="24" rx="2"/><path d="M20 12v16M24 15h-6a2.5 2.5 0 0 0 0 5h4a2.5 2.5 0 0 1 0 5h-6"/></svg>
    <h3>Pricing</h3><span>Lorem Ipsum is simply dummy text of the printing and typesetting industry.</span>
  </div>
  <div class="feature" style="left:628px;top:332px">
    <svg viewBox="0 0 40 40" fill="none" stroke="#1d3a6b" stroke-width="2"><circle cx="20" cy="16" r="7"/><path d="M8 20v-4a12 12 0 0 1 24 0v4M10 34a10 8 0 0 1 20 0"/></svg>
    <h3>Customer Support</h3><span>Lorem Ipsum is simply dummy text of the printing and typesetting industry.</span>
  </div>
  <div class="feature" style="left:844px;top:332px">
    <svg viewBox="0 0 40 40" fill="none" stroke="#1d3a6b" stroke-width="2"><path d="M20 34S6 25 6 15a7 7 0 0 1 14-2 7 7 0 0 1 14 2c0 10-14 19-14 19z"/></svg>
    <h3>We Value</h3><span>Lorem Ipsum is simply dummy text of the printing and typesetting industry.</span>
  </div>
</section>

<section class="testimonials">
  <h2 class="section-title">Testimonials</h2>
  <article class="review" style="left:-100px">
    <div class="who"><span class="avatar"></span><div><b>JOHN DOE</b><span class="stars">★★★★★</span></div></div>
    <span class="quote">”</span>
    <p>When an unknown printer took a galley of type and scrambled it to make a type specimen book. It has survived not only five centuries, but also the leap into electronic typesetting.</p>
  </article>
  <article class="review" style="left:380px;top:3780px">
    <div class="who"><span class="avatar"></span><div><b>JOHN DOE</b><span class="stars">★★★★★</span></div></div>
    <span class="quote">”</span>
    <p>When an unknown printer took a galley of type and scrambled it to make a type specimen book. It has survived not only five centuries, but also the leap into electronic typesetting.</p>
  </article>
  <article class="review" style="left:860px">
    <div class="who"><span class="avatar"></span><div><b>JOHN DOE</b><span class="stars">★★★★★</span></div></div>
    <span class="quote">”</span>
    <p>When an unknown printer took a galley of type and scrambled it to make a type specimen book. It has survived not only five centuries, but also the leap into electronic typesetting.</p>
  </article>
  <span class="t-arrow" style="left:368px;top:3912px"><svg viewBox="0 0 10 10"><path d="M7 1L3 5l4 4" fill="none" stroke="currentColor" stroke-width="2"/></svg></span>
  <span class="t-arrow" style="left:806px;top:3912px"><svg viewBox="0 0 10 10"><path d="M3 1l4 4-4 4" fill="none" stroke="currentColor" stroke-width="2"/></svg></span>
</section>

<footer class="site-footer">
  <div class="abs brand"><span class="brand-mark"></span><span class="brand-name">BRISA DECK</span></div>
  <div class="contact" style="left:128px"><span class="ic"><svg viewBox="0 0 18 18"><path d="M4 2h3l1.5 4-2 1.5a9 9 0 0 0 4 4L12 9.5l4 1.5v3a2 2 0 0 1-2 2A13 13 0 0 1 2 4a2 2 0 0 1 2-2z" fill="#fff"/></svg></span><span>CALL : <b>555 - 6777 - 555</b></span></div>
  <div class="contact" style="left:420px"><span class="ic"><svg viewBox="0 0 18 18"><rect x="2" y="4" width="14" height="10" fill="none" stroke="#fff" stroke-width="1.5"/><path d="M2 4l7 6 7-6" fill="none" stroke="#fff" stroke-width="1.5"/></svg></span><span>EMAIL : <b>LOREM@IPSUM.COM</b></span></div>
  <div class="contact" style="left:780px"><span class="ic"><svg viewBox="0 0 18 18"><path d="M3 3h12v9H7l-4 3z" fill="none" stroke="#fff" stroke-width="1.5"/></svg></span><span>LOREM IPSUM IS SIMPLY DUMMY</span></div>
  <nav class="foot-links">
    <a style="left:128px">Home</a><a style="left:296px">About US</a><a style="left:492px">Residential Rinks</a><a style="left:738px">Commercial Rinks</a><a style="left:996px">Contact Us</a>
  </nav>
  <div class="copyright">Copyright © 2022 BRISA DECK. All rights reserved.</div>
</footer>

</body>
</html>
```